Gratulation zur Firmengründung
Zielgruppe
Wir sind eine Steuerberatungskanzlei. Das Design soll potentiellen Neukunden gefallen!
Aufgabenstellung
Wir möchten einen Flyer im Format 21x9,8 erstellen. Eine Skizzierung der Idee findet sich in der angefügten Datei.

```html
<!DOCTYPE html>
<html lang="de">
<head>
<meta charset="utf-8">
<title>Gratulation zur Firmengründung – Flyer</title>
<link href="https://fonts.googleapis.com/css2?family=Crimson+Pro:ital,wght@0,400;1,400&display=swap" rel="stylesheet">
<style>
  :root {
    --green: #6a9a1c;
    --green-dark: #557d16;
    --green-deep: #3a4526;
    --green-deep-side: #2b3319;
    --cake: #c9dcb0;
    --ink: #1c1c1c;
    --white: #ffffff;
    --backdrop: #e4e4e4;
    --chart-bg: #f4f6f1;
  }
  html, body {
    margin: 0;
    width: 1200px;
    height: 1200px;
    overflow: hidden;
    background: var(--backdrop);
  }
  .sheet {
    position: absolute;
    left: 114px;
    width: 972px;
    height: 453px;
    background: var(--white);
  }
  .sheet--front { top: 96px; }
  .sheet--back  { top: 577px; }
  .sheet svg { display: block; }
  .serif { font-family: "Crimson Pro", Georgia, serif; }
  .headline { font-style: italic; fill: var(--green); }
  .band { fill: var(--green); }
  .band-text { font-style: italic; fill: var(--white); font-size: 29px; }
  .contact { fill: var(--white); font-size: 16px; }
  .brand { fill: var(--ink); font-size: 36px; font-style: italic; }
  .slice-label { fill: var(--ink); font-size: 16px; font-style: italic; }
  .leader { stroke: var(--ink); stroke-width: 1; fill: none; }
  .slice-main { fill: var(--green); }
  .slice-main-side { fill: var(--green-dark); }
  .slice-accent { fill: var(--green-deep); }
  .slice-accent-side { fill: var(--green-deep-side); }
  .chart-bg { fill: var(--chart-bg); }
</style>
</head>
<body>

<section class="sheet sheet--front">
  <svg width="972" height="453" viewBox="0 0 972 453" class="serif">
    <defs>
      <linearGradient id="cakeTone" x1="0" y1="0" x2="0" y2="1">
        <stop offset="0" stop-color="#ffffff"/>
        <stop offset="0.25" stop-color="#d3e3bd"/>
        <stop offset="0.8" stop-color="#c3d8a7"/>
        <stop offset="1" stop-color="#eef0ec"/>
      </linearGradient>
    </defs>
    <text class="headline" x="46" y="150" font-size="69">Wir</text>
    <text class="headline" x="142" y="183" font-size="40">gratulieren zur</text>
    <text class="headline" x="46" y="248" font-size="65">Firmengründung!</text>

    <rect x="608" y="23" width="321" height="323" fill="url(#cakeTone)" role="img" aria-label="Foto: hellgrüne Torte auf einem Tortenständer mit einer Kerze in Form einer Null"/>

    <rect class="band" x="0" y="347" width="585" height="69"/>
    <text class="band-text" x="47" y="391">Haben Sie steuerliche Fragen?</text>

    <text class="brand" x="643" y="390">kanzleiweg.de</text>
  </svg>
</section>

<section class="sheet sheet--back">
  <svg width="972" height="453" viewBox="0 0 972 453" class="serif">
    <text class="headline" x="48" y="96" font-size="32">Wir bieten individuelle</text>
    <text class="headline" x="48" y="133" font-size="32">Beratung für</text>
    <text class="headline" x="48" y="169" font-size="32">Ihr Unternehmen.</text>

    <rect class="chart-bg" x="476" y="89" width="354" height="256"/>

    <g class="pie-chart" transform="translate(643,212) scale(1,0.62)">
      <g transform="translate(0,28)">
        <path class="slice-main-side" d="M0 0 L-145 0 A145 145 0 0 1 145 0 Z"/>
        <path class="slice-main-side" d="M0 0 L83 119 A145 145 0 0 1 -145 0 Z"/>
        <path class="slice-accent-side" transform="translate(22,14)" d="M0 0 L145 0 A145 145 0 0 1 83 119 Z"/>
      </g>
      <path class="slice-main" d="M0 0 L-145 0 A145 145 0 0 1 145 0 Z"/>
      <path class="slice-main" d="M0 0 L83 119 A145 145 0 0 1 -145 0 Z"/>
      <path class="slice-accent" transform="translate(22,14)" d="M0 0 L145 0 A145 145 0 0 1 83 119 Z"/>
    </g>

    <text class="slice-label" x="474" y="91">Steuerberatung</text>
    <polyline class="leader" points="474,96 633,96 633,138"/>

    <text class="slice-label" x="334" y="209">Unternehmensberatung</text>
    <polyline class="leader" points="334,215 560,215 560,256"/>

    <text class="slice-label" x="808" y="213">Rechnungswesen</text>
    <polyline class="leader" points="926,219 766,219 766,259"/>

    <rect class="band" x="0" y="346" width="585" height="69"/>
    <text class="contact" x="46" y="376">Lindenallee 14</text>
    <text class="contact" x="46" y="398">20144 Hamburg</text>
    <text class="contact" x="203" y="376">Tel.: 040/555 012 345</text>
    <text class="contact" x="207" y="398">E-Mail: hamburg@kanzleiweg.de</text>

    <text class="brand" x="649" y="381">kanzleiweg.de</text>
  </svg>
</section>

</body>
</html>
```